Window Perf design with eadership quotes

I am wanting to create a window perf that covers windows in a conference room. I have included a picture of the windows. Each window is 26 1/2 inches by 92 inches. I have also included several other pictures to give an example of how I would like the Quotes to look.

Some Quotes I would like to use
1. Your Future is created by what you do today not tomorrow.
2. The answer is Yes
3. People don't care how much you know until they know how much you care.
4. Treat employees like they make a difference and they will.
5. Don't follow the crowd, Let the crowd follow you.
6. Treat people as if they were what they ought to be , and help them become what they are capable of being.
7. Leadership is not a title, its a behavior. LIVE IT
8. We make a living by what we get, We make a life by what we give.
9. Success is not final, failure is not fatal: it is courage to continue that counts.
10. The best way to predict your future is to create it.
11. The supreme quality of leadership is Integrity.
12. Whatever you are, Be a good one

Quotes

• I am imore interested in how this looks rather than including all of the quotes. I also ant this to be a solid background design for privacy.

```html
<!DOCTYPE html>
<html lang="en">
<head>
<meta charset="utf-8">
<title>Window Perf – The Best Way to Predict the Future</title>
<link rel="stylesheet" href="https://fonts.googleapis.com/css2?family=Montserrat:wght@700;800&family=Kaushan+Script&display=swap">
<style>
  :root {
    --bg: #050607;
    --white: #ffffff;
    --red: #e3202a;
    --yellow: #ffdc00;
  }
  html, body {
    margin: 0;
    padding: 0;
    width: 1200px;
    height: 4166px;
    overflow: hidden;
    background: var(--bg);
  }
  .window-perf {
    position: relative;
    width: 1200px;
    height: 4166px;
    background: var(--bg);
  }
  .quote-line {
    position: absolute;
    left: 0;
    width: 1200px;
    margin: 0;
    text-align: center;
    white-space: nowrap;
    line-height: 1;
  }
  .quote-line--bold {
    font-family: "Montserrat", Arial, sans-serif;
    font-weight: 800;
    color: var(--white);
    text-transform: uppercase;
  }
  .quote-line--large {
    font-size: 168px;
    letter-spacing: -0.075em;
    word-spacing: -0.05em;
  }
  .quote-line--small {
    font-size: 128px;
    letter-spacing: -0.03em;
  }
  .quote-line--script {
    font-family: "Kaushan Script", cursive;
    font-size: 262px;
    font-weight: 400;
  }
  .accent-red { color: var(--red); }
  .accent-yellow { color: var(--yellow); }

  .line-best-way { top: 1277px; }
  .line-to       { top: 1508px; }
  .line-predict  { top: 1598px; }
  .line-future   { top: 1973px; }
  .line-is-to    { top: 2252px; }
  .line-create   { top: 2420px; }
  .line-it       { top: 2717px; }
</style>
</head>
<body>
  <main class="window-perf">
    <p class="quote-line quote-line--bold quote-line--large line-best-way">The Best Way</p>
    <p class="quote-line quote-line--bold quote-line--small line-to">To</p>
    <p class="quote-line quote-line--script accent-red line-predict">Predict</p>
    <p class="quote-line quote-line--bold quote-line--large line-future">The Future</p>
    <p class="quote-line quote-line--bold quote-line--small line-is-to">Is To</p>
    <p class="quote-line quote-line--script accent-yellow line-create">Create</p>
    <p class="quote-line quote-line--bold quote-line--large line-it">It</p>
  </main>
</body>
</html>
```